Mouse and Rodent Infestation Spray

Need to Design label for 16oz bottle. The image sent has our initial design on it. Need other options.

Industry/Entity Type

Pest Control

Colors

Designer to choose colors to be used in the design.

```html
<!DOCTYPE html>
<html lang="en">
<head>
<meta charset="utf-8">
<title>NestOff Mouse &amp; Rat Infestation Labels</title>
<link href="https://fonts.googleapis.com/css2?family=Ubuntu:wght@500;700&family=Open+Sans:wght@600;700&family=Roboto+Condensed:wght@400;700&display=swap" rel="stylesheet">
<style>
  :root{
    --bg:#d4d4d4;
    --paper:#fbfbfb;
    --green:#2e9e3a;
    --green-dark:#1f8a2c;
    --green-light:#7cc242;
    --navy:#1f3590;
    --red:#d8262c;
    --grey:#6d6d6d;
    --gold:#c99a2e;
    --ink:#222;
  }
  *{box-sizing:border-box;margin:0;padding:0}
  html,body{width:1200px;height:1200px;overflow:hidden;background:var(--bg)}
  .stage{position:relative;width:1200px;height:1200px}
  .label{position:absolute;top:290px;width:540px;height:620px;background:var(--paper);overflow:hidden;box-shadow:0 2px 8px rgba(0,0,0,.12)}
  .label--front{left:40px}
  .label--back{left:620px}
  .band{position:absolute;left:0;bottom:0;width:540px;height:200px;z-index:0}
  .brand-shield{position:absolute;left:122px;top:0;width:300px;height:156px}
  .brand-name{position:absolute;left:122px;width:300px;top:48px;text-align:center;font-family:"Ubuntu",sans-serif;font-weight:700;font-size:34px;letter-spacing:3px;color:#fff;display:flex;justify-content:center;align-items:center;gap:8px}
  .brand-dot{width:12px;height:12px;border-radius:50%;background:#fff}
  .title-rule{position:absolute;left:110px;width:320px;border-top:1.5px dotted var(--red)}
  .title{position:absolute;left:0;width:540px;text-align:center;font-family:"Ubuntu",sans-serif;font-weight:700;color:var(--navy);line-height:.95;letter-spacing:1px}
  .chevron{position:absolute;left:170px;width:200px;height:22px}
  .tagline{position:absolute;left:0;width:540px;text-align:center;font-family:"Open Sans",sans-serif;font-weight:600;color:var(--grey);letter-spacing:.5px}
  .features{position:absolute;top:362px;left:0;width:540px;display:flex;justify-content:center;gap:32px}
  .feature{width:58px;height:58px;border-radius:50%;background:var(--green);color:#fff;font-family:"Roboto Condensed",sans-serif;font-weight:700;font-size:9px;line-height:1.1;text-align:center;display:flex;flex-direction:column;align-items:center;justify-content:center;gap:3px;box-shadow:0 0 0 2px #fff,0 0 0 3px var(--green)}
  .feature svg{width:14px;height:14px}
  .seal{position:absolute;z-index:2;border-radius:50%;background:radial-gradient(circle,#f2cd5c 0 55%,var(--gold) 56%)}
  .seal::after{content:"";position:absolute;inset:18%;border-radius:50%;background:#1b1b1b}
  .art{position:absolute;z-index:2;background:linear-gradient(160deg,#8cc63f,#2e9e3a);clip-path:polygon(50% 0,100% 15%,95% 70%,50% 100%,5% 70%,0 15%)}
  .pill{position:absolute;z-index:2;background:var(--navy);color:#fff;border-radius:14px;font-family:"Roboto Condensed",sans-serif;font-weight:700;display:flex;align-items:center;justify-content:center;box-shadow:0 0 0 2px #fff}
  .pill--advanced{left:68px;width:126px;height:34px;font-size:13px;line-height:1;color:#f6d21b;text-align:center;gap:6px}
  .pill--advanced svg{width:18px;height:22px}
  .pill--size{left:220px;width:98px;height:22px;font-size:11px}
  .cert{position:absolute;z-index:2;background:#fff;border:2px solid var(--navy)}
  .story{position:absolute;left:106px;top:314px;width:328px;font-family:"Roboto Condensed",sans-serif;font-size:7.6px;line-height:9.6px;color:var(--ink);text-align:justify}
  .story p+p{margin-top:9px}
  .story p:last-child{text-align-last:center}
</style>
</head>
<body>
<main class="stage">

  <section class="label label--front">
    <svg class="band" viewBox="0 0 540 200" preserveAspectRatio="none" aria-hidden="true">
      <path d="M0 60Q270 125 540 5V200H0Z" fill="var(--green-light)"/>
      <path d="M0 85Q270 150 540 35V200H0Z" fill="var(--green)"/>
    </svg>
    <svg class="brand-shield" viewBox="0 0 300 156" aria-hidden="true">
      <path d="M0 0H300V110L150 156L0 110Z" fill="var(--green-dark)"/>
      <path d="M10 0H290V104L150 146L10 104Z" fill="var(--green)"/>
      <path d="M60 0H200L10 90V40Z" fill="var(--green-light)" opacity=".35"/>
    </svg>
    <div class="brand-name">NEST<span class="brand-dot"></span>OFF</div>
    <div class="title-rule" style="top:164px"></div>
    <h1 class="title" style="top:174px;font-size:54px">MOUSE &amp; RAT<br>INFESTATION</h1>
    <div class="title-rule" style="top:288px"></div>
    <svg class="chevron" style="top:292px" viewBox="0 0 200 22" aria-hidden="true">
      <path d="M0 2H80L100 14L120 2H200" fill="none" stroke="var(--navy)" stroke-width="3"/>
      <path d="M70 10H85L100 20L115 10H130" fill="none" stroke="var(--red)" stroke-width="2"/>
    </svg>
    <p class="tagline" style="top:326px;font-size:18px">SAFE FOR INDOOR &amp; OUTDOOR USE</p>
    <div class="features">
      <div class="feature"><svg viewBox="0 0 14 14"><path d="M2 12C2 5 6 2 12 2C12 8 9 12 2 12Z" fill="#fff"/></svg>NATURAL<br>BAIT</div>
      <div class="feature"><svg viewBox="0 0 14 14"><rect x="4" y="3" width="6" height="10" rx="1" fill="#fff"/><rect x="5" y="1" width="4" height="2" fill="#fff"/></svg>PESTICIDE<br>FREE</div>
      <div class="feature"><svg viewBox="0 0 14 14"><path d="M2 7L6 11L12 3" fill="none" stroke="#fff" stroke-width="2"/></svg>LONG<br>LASTING</div>
    </div>
    <div class="seal" style="left:81px;top:428px;width:66px;height:66px"></div>
    <div class="art" role="img" aria-label="Shield emblem with crossed-out rat illustration" style="left:216px;top:428px;width:80px;height:110px"></div>
    <div class="pill pill--advanced" style="top:560px"><svg viewBox="0 0 18 22"><path d="M11 0L2 13H8L6 22L16 8H10Z" fill="#f6d21b"/></svg>ADVANCED<br>FORMULA</div>
    <div class="pill pill--size" style="top:569px">128 OZ &nbsp;|&nbsp; 1 GAL</div>
    <div class="seal" style="left:331px;top:562px;width:36px;height:36px"></div>
    <div class="cert" style="left:394px;top:556px;width:38px;height:42px;border-radius:50%"></div>
    <div class="cert" style="left:440px;top:548px;width:34px;height:54px;border-radius:4px"></div>
  </section>

  <section class="label label--back">
    <svg class="band" viewBox="0 0 540 200" preserveAspectRatio="none" aria-hidden="true">
      <path d="M0 62Q270 125 540 25V200H0Z" fill="var(--green-light)"/>
      <path d="M0 85Q270 150 540 50V200H0Z" fill="var(--green)"/>
    </svg>
    <svg class="brand-shield" viewBox="0 0 300 156" aria-hidden="true">
      <path d="M0 0H300V110L150 156L0 110Z" fill="var(--green-dark)"/>
      <path d="M10 0H290V104L150 146L10 104Z" fill="var(--green)"/>
      <path d="M60 0H200L10 90V40Z" fill="var(--green-light)" opacity=".35"/>
    </svg>
    <div class="brand-name">NEST<span class="brand-dot"></span>OFF</div>
    <div class="title-rule" style="top:160px"></div>
    <h2 class="title" style="top:166px;font-size:45px">MOUSE &amp; RAT<br>INFESTATION</h2>
    <svg class="chevron" style="top:258px" viewBox="0 0 200 22" aria-hidden="true">
      <path d="M0 2H80L100 14L120 2H200" fill="none" stroke="var(--navy)" stroke-width="3"/>
      <path d="M70 10H85L100 20L115 10H130" fill="none" stroke="var(--red)" stroke-width="2"/>
    </svg>
    <p class="tagline" style="top:286px;font-size:13px">SAFE FOR INDOOR &amp; OUTDOOR USE</p>
    <div class="story">
      <p>In 1903, rats ravaged a poor Romanian village, damaging all the food they stored for winter. So Avram Feld took it upon himself to repel the rodents and prevent them from returning. Using ground mint leaves and a few other secret ingredients, he non-lethally removed the rodents and saved the remaining rations. Avram passed the secret formula down to his children, and now six generations later, the Feld family is proud to pass the ultimate solution for rodent control on to you.</p>
      <p>From the founders of Burrow Guard, NestOff is the patented 3-in-1 formula to repel and prevent mouse and rat infestation. And with a few simple sprays, you can also help neutralize pheromones and help deodorize urine and droppings, just like the professionals! So, reclaim your space with a minty fresh blast of NestOff, the only rodent control solution you will ever need.</p>
    </div>
    <div class="seal" style="left:96px;top:460px;width:66px;height:66px"></div>
    <div class="art" role="img" aria-label="Shield emblem with crossed-out rat illustration" style="left:223px;top:454px;width:83px;height:96px"></div>
    <div class="pill pill--advanced" style="top:560px"><svg viewBox="0 0 18 22"><path d="M11 0L2 13H8L6 22L16 8H10Z" fill="#f6d21b"/></svg>ADVANCED<br>FORMULA</div>
    <div class="pill pill--size" style="top:569px">128 OZ &nbsp;|&nbsp; 1 GAL</div>
    <div class="seal" style="left:331px;top:562px;width:36px;height:36px"></div>
    <div class="cert" style="left:394px;top:556px;width:38px;height:42px;border-radius:50%"></div>
    <div class="cert" style="left:440px;top:548px;width:34px;height:54px;border-radius:4px"></div>
  </section>

</main>
</body>
</html>
```